Progressive and innovative Russian bank needs Landing Page for debit card with APR profit 9%

We need a web-design of the Landing Page for our new online retail financial service for Russian customers, debit card, named 'Harvest Card'. Harvest Card - is the debit stand-alone card (debit card not linked to a term deposit). Clients is getting profit (% on it's cash balance) depending on amount of cash:
- up to 30000₽ - 0%, 30000.01-700000₽ - 9% APR, more 700000₽ - 5% APR
- up to 1000$/€ - 0%, 1000-15000$/€ - 4% APR, more 15000$/€ - 2% APR
Clients can use the card as usual debit card for purchases in shops and payments (via internet too), etc. Traffic to the Landing Page come from ads in Searlo and Vokrum (Russian Searlo). We would like to see designs that use our brand colors and logo. The final design should follow brand limitations. Files in psd format.
Северный Вековой Банк

Reason: Thank you all. Our task was to make design of Landing page of the product. Majority of designs was the design of corporate site webpage. Please refine on your design.

```html
<!DOCTYPE html>
<html lang="en">
<head>
<meta charset="utf-8">
<title>Harvest Card — Северный Вековой Банк</title>
<link href="https://fonts.googleapis.com/css2?family=Roboto:ital,wght@0,400;0,500;0,700;1,400&family=Roboto+Condensed:wght@400;700&display=swap" rel="stylesheet">
<style>
:root{
  --navy:#0d4f9a;
  --navy-dark:#0a3f7d;
  --lime:#c6cf22;
  --lime-text:#c9d62b;
  --green:#6a9a1a;
  --sky:#dcedf9;
  --ink:#333;
  --muted:#666;
  --rule:#d6dde6;
  --yellow:#e8d400;
  --white:#fff;
}
*{box-sizing:border-box;margin:0;padding:0}
html,body{width:748px;height:1200px;overflow:hidden}
body{position:relative;background:var(--white);font-family:"Roboto",Arial,sans-serif;color:var(--ink)}
.abs{position:absolute}
a{color:inherit;text-decoration:none}

.topbar{left:0;top:0;width:748px;height:33px;background:var(--sky)}
.topbar .phones{left:50px;top:9px;font:italic 500 12px "Roboto",sans-serif;color:#555;display:flex;align-items:center;gap:5px}
.topbar .links{right:47px;top:10px;font-size:9px;color:var(--navy);letter-spacing:.2px}
.topbar .links span{color:#999;margin:0 4px}

.header{left:0;top:33px;width:748px;height:68px;border-bottom:1px solid #e6e6e6}
.brand{left:46px;top:8px;display:flex;align-items:center;gap:6px}
.brand .name{font:700 14px/17px "Roboto",sans-serif;color:var(--navy);width:86px}
.nav{left:186px;top:22px;display:flex;gap:20px;align-items:center;font:500 9.5px "Roboto",sans-serif;color:#555;letter-spacing:.3px}
.nav .active{background:var(--navy);color:var(--white);padding:7px 10px;border-radius:2px}

.hero{left:0;top:101px;width:748px;height:306px;background:linear-gradient(90deg,#eceff1 0%,#e4e7ea 50%,#d9dde0 100%)}
.hero .photo{left:360px;top:0;width:388px;height:306px;background:linear-gradient(135deg,#e7eaee 0%,#cfc6c0 40%,#b98a7c 60%,#e5e8ea 100%)}
.hero .kicker{left:47px;top:62px;font:400 19px/20px "Roboto Condensed",sans-serif;color:var(--navy);text-transform:uppercase}
.hero h1{left:46px;top:122px;font:700 35px "Roboto Condensed",sans-serif;color:var(--green);text-transform:uppercase;letter-spacing:.5px}
.hero .lede{left:47px;top:165px;width:300px;font:400 13px/17px "Roboto Condensed",sans-serif;color:#333}
.hero .cta{left:58px;top:228px;height:30px;padding:0 13px 0 16px;background:var(--navy);color:var(--white);border:2px solid #fff;box-shadow:0 0 0 1px var(--navy);border-radius:16px;font:500 13px/26px "Roboto Condensed",sans-serif;display:flex;gap:8px;align-items:center}

.rates{top:407px;height:75px;display:flex;align-items:center;padding-left:46px;font:700 15.5px/24px "Roboto",sans-serif}
.rates.rub{left:0;width:374px;background:var(--navy);color:var(--lime-text)}
.rates.fx{left:374px;width:374px;background:var(--lime);color:var(--navy);padding-left:25px}

.tile{top:503px;width:203px;height:116px;overflow:hidden}
.tile .bar{height:29px;background:var(--navy);color:var(--white);font:700 12px/31px "Roboto",sans-serif;padding-left:12px;letter-spacing:.2px}
.tile .pic{height:87px}
.tile.lead{background:linear-gradient(135deg,#1d5fa8,#134f93);border:1px solid var(--navy-dark)}
.tile.lead .title{position:absolute;left:11px;top:12px;font:700 12px "Roboto",sans-serif;color:#fff}
.tile.lead p{position:absolute;left:12px;top:34px;width:180px;font:9.5px/13px "Roboto",sans-serif;color:#dbe6f3}

.col-head{top:643px;width:202px;padding-bottom:4px;border-bottom:1px solid var(--rule);font:700 12px "Roboto",sans-serif;color:var(--navy);letter-spacing:.3px}
.intro{left:46px;top:676px;width:195px;font:9.5px/12px "Roboto",sans-serif;color:#555}
.partner{width:94px;height:67px;background:#fff;box-shadow:0 0 0 1px #eee,0 1px 3px rgba(0,0,0,.12);display:flex;align-items:center;justify-content:center}
.partner i{display:block;background:#d5dde6}

.news{left:273px;width:202px;height:66px;border-bottom:1px solid #e5e5e5;display:flex;gap:10px}
.news .date{width:26px;text-align:center}
.news .date b{display:block;border:1px solid #ccc;background:#fff;font:700 13px/19px "Roboto",sans-serif;color:var(--navy)}
.news .date span{font-size:8.5px;color:#777}
.news h3{font:500 9.5px "Roboto",sans-serif;color:var(--navy);margin-bottom:4px}
.news p{font:8.5px/11.5px "Roboto",sans-serif;color:#666;width:162px}
.news p a{color:var(--green)}

.hotline{left:500px;top:673px;width:202px;font:8.8px/15.6px "Roboto",sans-serif;color:#666}
.video{left:498px;top:800px;width:203px;height:153px;background:linear-gradient(135deg,#2f2f2f,#5c5450 55%,#3a3a3a)}
.video .play{position:absolute;left:5px;top:4px;width:40px;height:22px;background:#fff;display:flex;align-items:center;justify-content:center}
.video h4{position:absolute;left:8px;top:102px;font:700 13px "Roboto",sans-serif;color:var(--yellow)}
.video p{position:absolute;left:8px;top:120px;width:185px;font:8.5px/11px "Roboto",sans-serif;color:#eee}

.more{top:967px;height:20px;padding:0 9px;background:#eceeef;color:var(--navy);font:9.5px/20px "Roboto",sans-serif;display:flex;gap:5px;align-items:center}

.footer{left:0;top:1016px;width:748px;height:184px;background:var(--navy);border-top:3px solid var(--yellow)}
.footer h5{font:700 12px "Roboto",sans-serif;color:var(--yellow)}
.links-list{left:46px;top:1048px}
.links-list ul{list-style:none;margin-top:13px}
.links-list li{font:8px/15.8px "Roboto",sans-serif;color:#b7c9e2}
.links-list li:first-child{color:var(--yellow)}
.links-list li::before{content:"▪ ";font-size:7px}
.address{left:265px;top:1048px;width:170px;font:8.3px/12px "Roboto",sans-serif;color:#b7c9e2}
.address h5{margin-bottom:9px}
.social{left:265px;top:1158px;display:flex;gap:6px}
.social span{width:19px;height:19px;border-radius:50%;background:#fff}
.newsletter{left:505px;top:1038px;width:197px;height:124px;background:#115db0;border-radius:14px 14px 0 0;overflow:hidden}
.newsletter .top{background:#1469c4;height:73px;padding:10px 14px}
.newsletter h6{font:700 14px "Roboto",sans-serif;color:#fff;margin-bottom:6px}
.newsletter p{font:8.5px/11.5px "Roboto",sans-serif;color:#fff}
.newsletter .field{position:absolute;left:13px;top:85px;width:134px;height:26px;background:#fff;border-radius:3px;font:italic 8px/26px "Roboto",sans-serif;color:#333;padding-left:7px}
.newsletter .send{position:absolute;left:157px;top:85px;width:26px;height:26px;border-radius:50%;background:var(--lime);display:flex;align-items:center;justify-content:center}
.copy{left:505px;top:1172px;font:7.5px "Roboto",sans-serif;color:#b7c9e2}
.copy b{color:#fff;font-weight:400;margin-left:4px}
</style>
</head>
<body>

<div class="abs topbar">
  <div class="abs phones">
    <svg width="14" height="14" viewBox="0 0 24 24"><path d="M6.6 10.8a15 15 0 0 0 6.6 6.6l2.2-2.2c.3-.3.7-.4 1-.2 1.1.4 2.3.6 3.6.6.6 0 1 .4 1 1V20c0 .6-.4 1-1 1A17 17 0 0 1 3 4c0-.6.4-1 1-1h3.5c.6 0 1 .4 1 1 0 1.3.2 2.5.6 3.6.1.3 0 .7-.2 1z" fill="#0d4f9a"/></svg>
    8.400.310.2020 &nbsp;/&nbsp; 8.400.310.4040
  </div>
  <div class="abs links">FEEDBACKBANK<span>|</span>OFFICESATMS<span>|</span>ONLINE SERVICE</div>
</div>

<header class="abs header">
  <div class="abs brand">
    <div class="name">Северный Вековой Банк</div>
    <svg width="14" height="14"><rect width="14" height="14" fill="#c6cf22"/></svg>
  </div>
  <nav class="abs nav">
    <a class="active">HOME</a><a>ABOUT US</a><a>FOR INDIVIDUALS</a><a>CORPORATE COSTOMESRS</a><a>POWER UPS</a><a>CONTACT US</a>
  </nav>
</header>

<section class="abs hero">
  <div class="abs photo" role="img" aria-label="Smiling woman holding a red bank card beside a laptop and shopping bags"></div>
  <div class="abs kicker">We make your dreamsachievable<br>making your dreams closer</div>
  <h1 class="abs">Harvest Card</h1>
  <p class="abs lede">Lorem ipsum dolor sit amet, consectetur adipiscing elit. Vestibulum feugiat eget augue id consectetur</p>
  <a class="abs cta">ORDER NOW <svg width="9" height="10" viewBox="0 0 9 10"><path d="M1 1l3.5 4L1 9M4.5 1L8 5 4.5 9" stroke="#fff" stroke-width="1.4" fill="none"/></svg></a>
</section>

<div class="abs rates rub">UP TO 30000 - 0%, 30000.01-700000 -<br>9% APR, MORE 700000 - 5% APR</div>
<div class="abs rates fx">UP TO 1000$/€ - 0%, 1000-15000$/€ -<br>4% APR, MORE 15000$/€ - 2% APR</div>

<div class="abs tile lead" style="left:46px">
  <div class="title">BANK PAYMENT USED</div>
  <p>Lorem ipsum dolor sit amet, co nsecte tur adipiscing elit Mae cenas lobortis eu erat sit amet sollicit fhudin.</p>
  <svg class="abs" style="left:14px;top:82px" width="26" height="20" viewBox="0 0 26 20"><path d="M1 10h22M15 2l8 8-8 8" stroke="#fff" stroke-width="2" fill="none"/></svg>
</div>
<div class="abs tile" style="left:273px">
  <div class="bar">SNACK USED CARD</div>
  <div class="pic" role="img" aria-label="Woman handing a card to a man across a café table" style="background:linear-gradient(135deg,#e9e6e2,#b9a292 50%,#8d8c8e)"></div>
</div>
<div class="abs tile" style="left:498px">
  <div class="bar">ONLINE SHOPING CARD</div>
  <div class="pic" role="img" aria-label="Woman shopping online with a card and laptop" style="background:linear-gradient(135deg,#dfe4e8,#c9b3a6 55%,#e4a36a)"></div>
</div>

<div class="abs col-head" style="left:46px">CUSTOMERS</div>
<div class="abs col-head" style="left:273px">NEWS EVENT</div>
<div class="abs col-head" style="left:500px">HOTLINE</div>

<p class="abs intro">Lorem ipsum dolor sit amet, consectetur adipiscing elit. Pellentesque a commodo quam. Quisque.</p>
<div class="abs partner" style="left:46px;top:723px"><i style="width:60px;height:14px"></i></div>
<div class="abs partner" style="left:153px;top:723px"><i style="width:68px;height:22px;background:#1e6b3a"></i></div>
<div class="abs partner" style="left:46px;top:805px"><i style="width:66px;height:14px;background:#c3cee0"></i></div>
<div class="abs partner" style="left:153px;top:805px"><i style="width:32px;height:34px;background:#1d2b4a"></i></div>
<div class="abs partner" style="left:46px;top:886px"><i style="width:72px;height:24px;background:#bde0b0"></i></div>
<div class="abs partner" style="left:153px;top:886px"><i style="width:60px;height:28px;background:#cfdaea"></i></div>

<div class="abs news" style="top:674px"><div class="date"><b>20</b><span>OCT</span></div><div><h3>Lorem Ipsum is simply dummy</h3><p>Lorem ipsum dolor sit amet, consectet adipiscing elit. Pellentesque a commo uisque sceleris... <a>Read More</a></p></div></div>
<div class="abs news" style="top:747px"><div class="date"><b>20</b><span>OCT</span></div><div><h3>Lorem Ipsum is simply dummy</h3><p>Lorem ipsum dolor sit amet, consectet adipiscing elit. Pellentesque a commo uisque sceleris... <a>Read More</a></p></div></div>
<div class="abs news" style="top:820px"><div class="date"><b>20</b><span>OCT</span></div><div><h3>Lorem Ipsum is simply dummy</h3><p>Lorem ipsum dolor sit amet, consectet adipiscing elit. Pellentesque a commo uisque sceleris... <a>Read More</a></p></div></div>
<div class="abs news" style="top:893px;border:0"><div class="date"><b>20</b><span>OCT</span></div><div><h3>Lorem Ipsum is simply dummy</h3><p>Lorem ipsum dolor sit amet, consectet adipiscing elit. Pellentesque a commo uisque sceleris... <a>Read More</a></p></div></div>

<p class="abs hotline">Lorem ipsum dolor sit amet, consectetur adipiscing elit. Pellentesque a commodo quam. Quisque scelerisque augue et vestibulum malesuada. Cras eu ante sagittis, mollis mauris quis, rhoncus velit. Nunc fringilla auctor quam at laoreet. Duis cursus est ac justo euismod vulputate. In auctor, odio id finibus maximus.</p>

<div class="abs video" role="img" aria-label="Video still of a woman holding a card">
  <div class="play"><svg width="10" height="11"><path d="M1 0l9 5.5L1 11z" fill="#111"/></svg></div>
  <h4>HARVEST CARD</h4>
  <p>Lorem ipsum dolor sit amet, consectetuorlor advlore Maecenas lobortis elit.</p>
</div>

<a class="abs more" style="left:106px">VIEW MORE <svg width="5" height="7"><path d="M0 0l5 3.5L0 7z" fill="#0d4f9a"/></svg></a>
<a class="abs more" style="left:332px">VIEW MORE <svg width="5" height="7"><path d="M0 0l5 3.5L0 7z" fill="#0d4f9a"/></svg></a>
<a class="abs more" style="left:558px">VIEW MORE <svg width="5" height="7"><path d="M0 0l5 3.5L0 7z" fill="#0d4f9a"/></svg></a>

<footer class="abs footer"></footer>
<div class="abs links-list">
  <h5>Other link</h5>
  <ul><li>Home</li><li>Order Now</li><li>How it works</li><li>Proven to work</li><li>Faq's</li><li>Testimonials</li><li>In the news</li><li>Contact us</li></ul>
</div>
<div class="abs address">
  <h5>Conatct Address</h5>
  <p>Lorem ipsum dolor sit amelo consectetur adipiscing elitlo Pellentesque.</p>
  <p style="margin-top:13px">Call: 400 310 2020</p>
  <p style="margin-top:12px">Email: hello@harvestcard-mail.net</p>
</div>
<div class="abs social"><span></span><span></span><span></span><span></span><span></span></div>

<div class="abs newsletter">
  <div class="top">
    <h6>Get Our Newsletter!</h6>
    <p>Lorem ipsum dolor sit amet, consectetur dipiscing elit. Pellentesque a commodo quam. Quisque scelerisque.</p>
  </div>
  <div class="field">Enter your email address</div>
  <div class="send"><svg width="12" height="12" viewBox="0 0 12 12"><path d="M1 1l10 5-10 5 2-5z" fill="#0d4f9a"/></svg></div>
</div>
<div class="abs copy">Copyright © 2014, <b>NORTHERN CENTURY BANK.</b></div>

</body>
</html>
```